Refresh Existing Tradeshow Expo Booth

Scope: We're looking for a refresh of our existing tradeshow booth materials.

Business: IT Company specializing in Education service and support of mobile technology. We repair, service and support schools Zorvas, Velnotes, Plumeslates and other technology.

Core Message: No-sign-ups, diagnostic fees, troubleshooting, or complicated invoicing. Just pack and ship, and we handle the rest.

Tagline: We make 1:1 repairs easy, fast, and affordable.

Additional Resources: https://www.quillbranch.com/for-education/

Deliverables:
1 - 72" x 30" Banner Stand
1 - 8' Table Cloth Throw
1 - 2.5' x 8' Banner
Included in .psd or .ai files ready to print.

Materials Provided:
Brand Usage Guide
Sample Flyers / Marketing Materials
Original Vertical Banner Stand / Banner
Sample Messaging

Target Market(s)

IT Directors, Education, ED Tech

Industry/Entity Type

IT, Education

Other font styles liked:
• Dekar, Dekar Light

Colors
EB3D1F
EC4F4E
F09395
F8D3D4
FCEDEE

Requirements
Must have
• Clean Design, Not Busy, Crisp Lines, Brand Colors.

```html
<!DOCTYPE html>
<html lang="en">
<head>
<meta charset="utf-8">
<title>Quillbranch Expo Booth – Table Cloth and Banner</title>
<link href="https://fonts.googleapis.com/css2?family=Montserrat:wght@400;500;700;800&family=Rajdhani:wght@300;400&family=Roboto+Condensed:wght@400;700&display=swap" rel="stylesheet">
<style>
  :root{
    --stage:#1e1e1e;
    --paper:#ffffff;
    --ink:#1a1a1a;
    --brand-red:#e81f27;
    --photo-light:#e9e4de;
    --photo-mid:#c9bfb3;
    --label:#f2f2f2;
  }
  *{margin:0;padding:0;box-sizing:border-box}
  html,body{width:1200px;height:1200px;overflow:hidden;background:var(--stage)}
  .board{position:relative;width:1200px;height:1200px;font-family:"Montserrat",sans-serif}

  /* Table cloth */
  .tablecloth{position:absolute;left:307px;top:81px;width:603px;height:603px;background:var(--paper)}
  .tablecloth__frame{position:absolute;inset:17px;border:1.5px solid var(--brand-red)}
  .tablecloth__mark{position:absolute;left:251px;top:225px;width:100px;height:100px;border-radius:50%;background:var(--brand-red)}
  .brand-name{font-family:"Rajdhani",sans-serif;font-weight:300;color:var(--ink);text-transform:uppercase;white-space:nowrap}
  .tablecloth__name{position:absolute;left:0;right:0;top:320px;text-align:center;font-size:60px;letter-spacing:7px;line-height:1}
  .service-line{font-weight:400;color:var(--ink);white-space:nowrap}
  .service-line strong{font-weight:700;color:var(--brand-red)}
  .tablecloth__service{position:absolute;left:0;right:0;top:384px;text-align:center;font-size:20px}
  .tablecloth__rule{position:absolute;left:230px;width:142px;top:418px;height:1.5px;background:var(--brand-red)}
  .tablecloth__cta{position:absolute;left:220px;top:529px;width:164px;height:13px;background:var(--brand-red);color:#fff;font-family:"Roboto Condensed",sans-serif;font-weight:700;font-size:10.5px;line-height:13px;text-align:center}
  .tablecloth__cta::after{content:"";position:absolute;left:76px;bottom:-5px;border:6px solid transparent;border-bottom:0;border-top:5px solid var(--brand-red)}
  .tablecloth__url{position:absolute;left:0;right:0;top:551px;text-align:center;font-size:18px;font-weight:500;color:var(--ink);letter-spacing:-0.3px}
  .tablecloth__url span{color:var(--brand-red);font-weight:700}

  .caption{position:absolute;left:0;right:0;text-align:center;color:var(--label);font-family:"Rajdhani",sans-serif;font-weight:400;font-size:28px;letter-spacing:0.5px}
  .caption--tablecloth{top:695px}
  .caption--banner{top:1126px}

  /* Banner */
  .banner{position:absolute;left:119px;top:800px;width:1000px;height:312px;background:var(--paper);overflow:hidden}
  .banner__name{position:absolute;left:70px;top:30px;font-size:50px;letter-spacing:9px;line-height:1}
  .banner__mark{position:absolute;left:72px;top:20px;width:0;height:0}
  .banner__service{position:absolute;left:97px;top:124px;font-size:21px}
  .features{position:absolute;left:64px;top:162px;display:flex;list-style:none}
  .feature{width:74.5px;display:flex;flex-direction:column;align-items:center}
  .feature__icon{width:60px;height:60px}
  .feature__label{margin-top:5px;font-size:6.5px;font-weight:700;color:var(--ink);text-align:center;line-height:1.25;letter-spacing:-0.1px}
  .banner__tagline{position:absolute;left:0;top:251px;width:640px;height:28px;background:#000;color:#fff;font-weight:800;font-size:18px;line-height:28px;padding-left:43px;letter-spacing:-0.2px}
  .banner__cta{position:absolute;left:0;top:279px;width:640px;height:33px;background:var(--brand-red);color:#fff;font-family:"Roboto Condensed",sans-serif;font-size:27px;line-height:33px;padding-left:50px;letter-spacing:-0.8px;white-space:nowrap}
  .banner__cta strong{font-family:"Montserrat",sans-serif;font-weight:700;letter-spacing:-0.5px;margin-left:8px;font-size:26px}
  .banner__art{position:absolute;left:0;top:0;width:1000px;height:312px}
</style>
</head>
<body>
<main class="board">

  <section class="tablecloth" aria-label="Table cloth">
    <div class="tablecloth__frame"></div>
    <div class="tablecloth__mark" aria-hidden="true"></div>
    <h1 class="brand-name tablecloth__name">Quillbranch</h1>
    <p class="service-line tablecloth__service">Plumeslate &amp; Zorva <strong>REPAIR SERVICES</strong></p>
    <div class="tablecloth__rule"></div>
    <p class="tablecloth__cta">REQUEST A FREE REPAIR</p>
    <p class="tablecloth__url">WWW.<span>QUILLBRANCH</span>.COM</p>
  </section>
  <p class="caption caption--tablecloth">TABLE CLOTH</p>

  <section class="banner" aria-label="Banner">
    <h2 class="brand-name banner__name">Quillbranch</h2>
    <p class="service-line banner__service">Plumeslate &amp; Zorva <strong>REPAIR SERVICES</strong></p>

    <ul class="features">
      <li class="feature">
        <svg class="feature__icon" viewBox="0 0 60 60"><circle cx="30" cy="30" r="29.5" fill="var(--brand-red)"/><circle cx="30" cy="30" r="27" fill="none" stroke="#fff" stroke-width="1"/>
          <g fill="#fff"><circle cx="30" cy="30" r="11"/><g stroke="#fff" stroke-width="6"><line x1="30" y1="14" x2="30" y2="46"/><line x1="14" y1="30" x2="46" y2="30"/><line x1="19" y1="19" x2="41" y2="41"/><line x1="41" y1="19" x2="19" y2="41"/></g></g>
          <circle cx="30" cy="30" r="5" fill="var(--brand-red)"/></svg>
        <span class="feature__label">FREE DIAGNOSTICS</span>
      </li>
      <li class="feature">
        <svg class="feature__icon" viewBox="0 0 60 60"><circle cx="30" cy="30" r="29.5" fill="var(--brand-red)"/><circle cx="30" cy="30" r="27" fill="none" stroke="#fff" stroke-width="1"/>
          <g fill="#fff"><circle cx="30" cy="22" r="4"/><rect x="25" y="27" width="10" height="14" rx="2"/><circle cx="20" cy="26" r="3"/><rect x="16" y="30" width="8" height="10" rx="2"/><circle cx="40" cy="26" r="3"/><rect x="36" y="30" width="8" height="10" rx="2"/></g>
          <path d="M20 18 A12 12 0 0 1 40 18" fill="none" stroke="#fff" stroke-width="1.5"/></svg>
        <span class="feature__label">LOCALLY OWNED</span>
      </li>
      <li class="feature">
        <svg class="feature__icon" viewBox="0 0 60 60"><circle cx="30" cy="30" r="29.5" fill="var(--brand-red)"/><circle cx="30" cy="30" r="27" fill="none" stroke="#fff" stroke-width="1"/>
          <path d="M30 12 L44 17 V30 C44 40 36 45 30 47 C24 45 16 40 16 30 V17 Z" fill="none" stroke="#fff" stroke-width="1.6"/>
          <circle cx="39" cy="40" r="7" fill="var(--brand-red)" stroke="#fff" stroke-width="1.6"/><path d="M39 36 V40 H42" fill="none" stroke="#fff" stroke-width="1.4"/></svg>
        <span class="feature__label">LIFETIME WARRANTY</span>
      </li>
      <li class="feature">
        <svg class="feature__icon" viewBox="0 0 60 60"><circle cx="30" cy="30" r="29.5" fill="var(--brand-red)"/><circle cx="30" cy="30" r="27" fill="none" stroke="#fff" stroke-width="1"/>
          <g fill="none" stroke="#fff" stroke-width="1.6"><rect x="21" y="22" width="16" height="13"/><path d="M37 26 H43 L47 31 V35 H37"/></g>
          <g fill="#fff"><circle cx="26" cy="37" r="2.5"/><circle cx="42" cy="37" r="2.5"/><rect x="11" y="25" width="8" height="1.4"/><rect x="13" y="29" width="7" height="1.4"/><rect x="10" y="33" width="9" height="1.4"/></g></svg>
        <span class="feature__label">FREE SHIPPING/<br>PICKUP</span>
      </li>
      <li class="feature">
        <svg class="feature__icon" viewBox="0 0 60 60"><circle cx="30" cy="30" r="29.5" fill="var(--brand-red)"/><circle cx="30" cy="30" r="27" fill="none" stroke="#fff" stroke-width="1"/>
          <rect x="15" y="18" width="17" height="13" fill="#fff"/><rect x="26" y="28" width="20" height="15" fill="#fff" stroke="var(--brand-red)" stroke-width="2"/><rect x="26" y="28" width="20" height="3" fill="var(--brand-red)"/></svg>
        <span class="feature__label">P.O. FRIENDLY</span>
      </li>
      <li class="feature">
        <svg class="feature__icon" viewBox="0 0 60 60"><circle cx="30" cy="30" r="29.5" fill="var(--brand-red)"/><circle cx="30" cy="30" r="27" fill="none" stroke="#fff" stroke-width="1"/>
          <circle cx="30" cy="30" r="15" fill="none" stroke="#fff" stroke-width="2"/>
          <text x="30" y="38" text-anchor="middle" font-family="Montserrat, sans-serif" font-weight="800" font-size="22" fill="#fff">$</text></svg>
        <span class="feature__label">VOLUME DISCOUNTS</span>
      </li>
    </ul>

    <p class="banner__tagline">WE MAKE 1:1 REPAIRS EASY, FAST, AND AFFORDABLE</p>
    <p class="banner__cta">REQUEST A FREE REPAIR <strong>(555) 014-2290</strong></p>

    <svg class="banner__art" viewBox="0 0 1000 312" aria-hidden="false">
      <defs>
        <linearGradient id="classroomTone" x1="0" y1="0" x2="1" y2="1">
          <stop offset="0" stop-color="var(--photo-light)"/>
          <stop offset="0.6" stop-color="#ddd5cb"/>
          <stop offset="1" stop-color="var(--photo-mid)"/>
        </linearGradient>
      </defs>
      <path d="M690 0 Q575 70 563 165 Q592 60 722 0 Z" fill="var(--brand-red)"/>
      <path d="M563 160 Q555 245 578 312 L604 312 Q583 230 600 150 Z" fill="#000"/>
      <path d="M722 0 Q600 70 597 160 Q592 240 608 312 L1000 312 L1000 0 Z" fill="url(#classroomTone)" role="img" aria-label="Photo: a teacher holding a tablet with three pupils at laptops in a bright classroom"/>
    </svg>
  </section>
  <p class="caption caption--banner">BANNER</p>

</main>
</body>
</html>
```